Create a Brochure Design for Brantley Homecare

Brantley Homecare is a subsidiary of the Brantley Care Group. This brochure is specifically for the Brantley Homecare company and brand. Create a 3 panel, A4, front and back, tri-fold brochure. This brochure will be a way to introduce our Homecare services to the community, prospective clients, and various referral partners. The brochure must be eye catching, unique in its deliverables and demonstrate both attention to detail and comfort. Our organization is sophisticated and built around warmth, care and individualized personal attention. The most important aspect of this design is to focus on creating a nurturing, warm, and inviting feel where you would want to have a Nurse or Nurse’s Aide in your own home or a loved one’s home.

I am open to the creativity of the designer to develop something based on the above criteria; however I would like the design to work well with the existing collateral material. What I mean by that is that while I want everything to have its own personality and stand out as its own brand representative, I still need to be able to tell that the overall design concept stays stylistically inside of the same ‘family’ of existing designed material. Because of this, below I would like for the designer to pull inspiration from the link to our website (Located below) as well as from the attachment of our recently refreshed business cards (Attached). This should allow each design to be unique and creative, while still staying inside of a framework and the feel/style that I am looking for.

Finally, I want all the designers to understand that this brochure design is for a private, in home, healthcare company where we are responsible for providing personalized care for a culturally and ethnically diverse make-up clientele of all ages. The photos that are used must represent an image of warmth, care, and a positive interaction between client and caregiver.

Look under the Brantley Homecare tab at www.brantleycaregroup-example.net

Industry/Entity Type

Healthcare

Requirements
Must have
• • The Brantley Homecare company logo must be included.

```html
<!DOCTYPE html>
<html lang="en">
<head>
<meta charset="utf-8">
<title>Brantley Homecare – Tri-fold Brochure</title>
<link rel="stylesheet" href="https://fonts.googleapis.com/css2?family=Arimo:wght@400;700&family=Oswald:wght@600;700&display=swap">
<style>
  :root {
    --teal: #0c7a6f;
    --teal-light: #14a08f;
    --salmon: #ee977f;
    --salmon-text: #e8826a;
    --orange: #f39a6c;
    --rule: #b5b5b5;
    --ink: #222;
    --body: #444;
    --photo-a: #d9cfc4;
    --photo-b: #eae4dc;
    --body-font: "Arimo", Arial, sans-serif;
    --title-font: "Oswald", "Arial Narrow", sans-serif;
  }
  * { box-sizing: border-box; margin: 0; padding: 0; }
  html, body { width: 1200px; height: 1000px; overflow: hidden; background: #fff; }
  body { position: relative; font-family: var(--body-font); color: var(--ink); }

  .spread { position: absolute; left: 78px; width: 569px; height: 397px; overflow: hidden; background: #fff; }
  .spread--outside { top: 46px; }
  .spread--inside { top: 548px; }
  .spread svg.shapes { position: absolute; inset: 0; width: 100%; height: 100%; }
  .abs { position: absolute; }

  .photo { position: absolute; background: linear-gradient(135deg, var(--photo-b), var(--photo-a)); box-shadow: 1px 2px 4px rgba(0,0,0,.35); }
  .photo--soft { box-shadow: none; background: radial-gradient(ellipse at 50% 55%, #d8b49c 0%, #ecd8c9 45%, rgba(255,255,255,0) 75%); }

  .placeholder { font-weight: 700; color: var(--salmon-text); }
  .placeholder--caps { font-size: 9.5px; letter-spacing: .2px; }
  .placeholder--lower { font-size: 12px; }

  .cover-title { font-family: var(--title-font); font-weight: 700; color: var(--teal); font-size: 25px; line-height: 29px; letter-spacing: .2px; }
  .cover-tagline { font-size: 7px; font-weight: 700; color: var(--orange); line-height: 10px; }

  .contact { font-size: 6.4px; line-height: 8.4px; font-weight: 700; color: var(--ink); }
  .contact .indent { padding-left: 42px; display: block; }

  .brand { display: flex; align-items: center; gap: 4px; }
  .brand__mark { width: 9px; height: 9px; background: var(--salmon); }
  .brand__name { font-family: var(--body-font); font-weight: 700; font-size: 11px; color: var(--teal); }

  .col { position: absolute; font-size: 6.6px; line-height: 8.4px; color: var(--body); }
  .col h2 { font-size: 9.5px; font-weight: 700; color: var(--salmon-text); line-height: 11px; }
  .col h3 { font-size: 7px; font-weight: 400; color: var(--orange); text-transform: uppercase; line-height: 9.5px; }
  .col .lead { color: var(--teal); }
  .col p + p, .col p + .lead, .col ul + .lead { margin-top: 6px; }
  .col ul { list-style: none; }
  .col--schedule { line-height: 8.3px; }
  .col--services { font-size: 6.6px; line-height: 9px; font-weight: 700; color: #333; }
  .col--services p { margin-bottom: 9px; }
  .col--services .term { color: var(--teal); }

  .label { position: absolute; font-family: var(--body-font); font-size: 17px; color: #111; }
</style>
</head>
<body>

<section class="spread spread--outside" aria-label="Outside of brochure: back panel and front cover">
  <svg class="shapes" viewBox="0 0 569 397" preserveAspectRatio="none" aria-hidden="true">
    <defs>
      <linearGradient id="outsideBg" x1="0" y1="0" x2="0" y2="1">
        <stop offset="0" stop-color="#e3e3e3"/>
        <stop offset=".65" stop-color="#ffffff"/>
      </linearGradient>
    </defs>
    <rect width="569" height="397" fill="url(#outsideBg)"/>
    <path d="M0,232 C150,240 230,200 320,120 C400,50 480,35 569,28 L569,40 C480,48 410,72 340,140 C250,228 150,275 0,276 Z" fill="var(--salmon)"/>
    <path d="M0,290 C150,286 250,232 340,152 C420,82 490,56 569,50" fill="none" stroke="var(--rule)" stroke-width="1"/>
    <path d="M0,378 C130,398 380,396 569,292 L569,308 C380,414 130,416 0,400 Z" fill="var(--salmon)"/>
  </svg>

  <div class="photo" style="left:33px;top:10px;width:135px;height:200px" role="img" aria-label="Photo of a smiling caregiver with an elderly client holding a cane"></div>
  <p class="abs placeholder placeholder--caps" style="left:205px;top:22px">YOU CAN ENTER UR DATA HERE</p>
  <p class="abs placeholder placeholder--lower" style="left:28px;top:298px">you can enter ur data here</p>

  <div class="abs contact" style="left:202px;top:338px">
    Address:&nbsp; 4870 Harbor Crest Ave., Suite 210
    <span class="indent">Lakeview, HI96700</span>
    tel.: (555) 014-4486<br>
    fax: (555) 014-4822<br>
    info@brantleyhomecare-example.com<br>
    www.brantleyhomecare-example.com
  </div>

  <h1 class="abs cover-title" style="left:400px;top:71px">QUALITY HOME<br>CARE SERVICES</h1>
  <p class="abs cover-tagline" style="left:400px;top:140px">SOME ONE YOU CAN DEPEND ON...<br>WITHOUT QUESTIONS...</p>
  <div class="photo photo--soft" style="left:386px;top:172px;width:183px;height:140px" role="img" aria-label="Photo of a caregiver's hand gently holding an elderly person's hand"></div>

  <div class="abs brand" style="left:500px;top:345px">
    <span class="brand__mark"></span><span class="brand__name">Brantley</span>
  </div>
</section>

<p class="label" style="left:150px;top:476px">4</p>
<p class="label" style="left:307px;top:466px">BACK</p>
<p class="label" style="left:474px;top:466px">FRONT</p>

<section class="spread spread--inside" aria-label="Inside of brochure: panels one to three">
  <svg class="shapes" viewBox="0 0 569 397" preserveAspectRatio="none" aria-hidden="true">
    <defs>
      <linearGradient id="tealBand" x1="0" y1="0" x2="1" y2="1">
        <stop offset="0" stop-color="var(--teal)"/>
        <stop offset="1" stop-color="var(--teal-light)"/>
      </linearGradient>
    </defs>
    <path d="M0,0 H569 V38 C460,60 320,58 210,42 C130,30 60,32 0,58 Z" fill="url(#tealBand)"/>
    <path d="M0,58 C60,32 130,30 210,42 C320,58 460,60 569,38" fill="none" stroke="#fff" stroke-width="1.5" opacity=".6"/>
    <path d="M0,318 C90,318 150,380 250,384 C380,390 500,354 569,320 V397 H0 Z" fill="var(--salmon)"/>
  </svg>

  <div class="col" style="left:25px;top:62px;width:166px">
    <h2>About Brantley Homecare</h2>
    <p>Brantley Homecare is a state-licensed private duty home health care agency serving the island community of Oahu since 1996. We provide in-home services ranging from light housekeeping to personal care and skilled nursing. We strive to give compassionate, dependable care of the highest quality while maintaining extremely competitive rates. Everything we do is geared toward meeting the individual needs of our clients.<br>
    Whether you need a little help or a lot of help, you'll find that Brantley Homecare's services are a cut above the rest. The Brantley Way is special; it is compassionate, professional, dependable, and flexible.</p>
    <p class="lead">All of our Care Professionals:</p>
    <ul>
      <li>Are bonded, insured, and supervised;</li>
      <li>Have passed both criminal and abuse background checks;</li>
      <li>Have been screened for TB;</li>
      <li>Are certified in CPR and First Aid</li>
    </ul>
    <p class="lead">All client care is supervised by a licensed Nurse Care Consultant whose duties include:</p>
    <ul>
      <li>Regular home visits</li>
      <li>Client evaluation</li>
      <li>Care Professional supervision</li>
      <li>Revising/updating client care plans</li>
      <li>24/7 phone support</li>
    </ul>
  </div>

  <div class="photo" style="left:207px;top:37px;width:142px;height:92px" role="img" aria-label="Photo of a nurse talking warmly with a seated elderly client"></div>
  <div class="col" style="left:207px;top:139px;width:188px">
    <h3>Services</h3>
    <p>Brantley Homecare provides two different levels of care. Our Nurse Care Consultant will assist the client and family in determining the appropriate level</p>
  </div>
  <div class="photo" style="left:207px;top:180px;width:142px;height:92px" role="img" aria-label="Photo of a caregiver and client chatting over cups of tea"></div>
  <div class="col col--schedule" style="left:207px;top:276px;width:190px">
    <h3>Your Schedule</h3>
    <p>Brantley Homecare is flexible with your care needs. As you need more or less care, your schedule can be adjusted to accommodate your needs. We have found that a set schedule works best (same days and times each week). This allows you to be able to depend on the same care professional(s) each week. You determine the schedule, from a minimum of four hours per shift to 24 hours of care per day, 7 days per week, 365 days per year. Our Scheduling department is available 24 hours per day.</p>
  </div>

  <div class="col col--services" style="left:400px;top:96px;width:160px">
    <p><span class="term">Nurse Aide Care</span> – Our Nurse Aides help you with your personal care needs, provide companionship, run errands, and do light housekeeping, along with assisting you with the activities of daily living.</p>
    <p><span class="term">Skilled Nursing Care</span> – We offer a wide range of skilled nursing services using RN's and LPN's who provide treatment from wound care to life support, in addition to all of the services performed by our Nurse Aides.</p>
    <p>Clients who already receive personal care services can also have the following additional support services.</p>
    <p><span class="term">Medication Services</span> – Our licensed nurse will pre-pour your medication in weekly pill containers for a 28-day period.</p>
    <p><span class="term">Transportation Services</span> – Our Care Professionals run errands or escort you to the grocery store, your personal appointments (physician, beautician, therapy), or other outings.</p>
  </div>
</section>

<p class="label" style="left:151px;top:953px">1</p>
<p class="label" style="left:370px;top:960px">2</p>
<p class="label" style="left:532px;top:960px">3</p>

</body>
</html>
```